Commercial painting company is looking for a creative website designer.

Hi, we just completed our logo project and now ready to launch our website. The project will be done on Squarespace platform. It will contain:
Page 1 HOME
Page 2 SERVICES
Page 3 PICTURES
The content will be written by us. I am not sure bout the pictures, I do not have any to provide. I can buy stock photos if needed.
We are commercial only painting company and have to appeal to commercial, industrial property mangers. We will need CALL, REQUEST FOR ESTIMATE buttons.
If possible to have a live picture on home page would be great. Thank you
Target Market(s)
Property Managers
Industry/Entity Type
Commercial Painting
Other font styles liked:
- Poppins

```html
<!DOCTYPE html>
<html lang="en">
<head>
<meta charset="utf-8">
<title>Keystone Pro Co</title>
<link href="https://fonts.googleapis.com/css2?family=Poppins:ital,wght@0,300;0,400;0,500;0,600;0,700;1,300;1,400&display=swap" rel="stylesheet">
<style>
:root{
  --navy:#022a6b;
  --red:#c3102f;
  --ink:#222;
  --muted:#555;
  --white:#fff;
  --rule:#d9d9d9;
}
*{margin:0;padding:0;box-sizing:border-box}
html,body{width:1200px;height:3573px;overflow:hidden}
body{position:relative;font-family:"Poppins",sans-serif;color:var(--ink);background:var(--white)}
.abs{position:absolute}

/* hero */
.hero{left:0;top:0;width:1200px;height:600px;background:linear-gradient(180deg,#5d86c4 0%,#a9bfdc 35%,#d9b978 60%,#8a7a5e 82%,#55604a 100%)}
.brand{left:111px;top:43px;display:flex;align-items:center;gap:10px;color:var(--navy);font-weight:600;font-size:18px}
.brand-dot{width:34px;height:34px;border-radius:50%;background:var(--white);border:3px solid var(--navy);flex:none}
.brand-text{background:rgba(255,255,255,.9);padding:4px 10px}
.nav{top:34px;left:393px;display:flex;gap:31px;font-size:15px;color:var(--white)}
.nav a{color:var(--white);text-decoration:none;padding-bottom:4px}
.nav a.active{color:var(--red);border-bottom:3px solid var(--red)}
.btn{background:var(--red);color:var(--white);font-weight:700;text-transform:uppercase;display:flex;align-items:center;justify-content:center;gap:8px;font-size:14px}
.call{left:904px;top:21px;width:184px;height:43px}
.hero-box{left:86px;top:223px;width:511px;min-height:221px;background:rgba(40,40,40,.62);padding:10px 22px 26px}
.hero-title{font-weight:400;font-size:51px;color:var(--white);line-height:1.2;white-space:nowrap}
.hero-text{font-size:15px;color:var(--white);line-height:26px;margin:12px 0 0 4px;width:450px}
.estimate{width:210px;height:43px;margin:17px 0 0 4px}

/* who */
.section-title{width:1200px;text-align:center;font-weight:400;color:var(--ink);text-transform:uppercase}
.who-title{top:690px;font-size:50px}
.who-text{left:209px;top:767px;width:775px;text-align:justify;text-align-last:center;font-size:15px;line-height:25.8px;color:var(--muted);font-weight:300}
.work-photo{left:0;top:990px;width:1200px;height:489px;background:linear-gradient(160deg,#d5d5d3 0%,#c4c4c2 55%,#8e8e8c 75%,#1f3a6b 100%)}

/* services */
.services{left:0;top:1479px;width:1200px;height:519px;background:var(--navy);color:var(--white)}
.services-title{top:90px;font-size:50px;color:var(--white)}
.service-divider{left:599px;top:169px;width:1px;height:248px;background:rgba(255,255,255,.6)}
.service{top:185px;width:420px;text-align:center}
.service-icon{height:76px;display:flex;align-items:flex-end;justify-content:center}
.service h3{font-weight:400;font-size:22px;margin-top:14px}
.service p{font-size:15px;line-height:26px;margin-top:10px;padding:0 80px}

/* testimonials */
.test-title{top:2080px;font-size:50px}
.test-photo{left:576px;top:2178px;width:383px;height:501px;background:linear-gradient(180deg,#4f86cc 0%,#a9c6e6 30%,#ddd6bd 55%,#3b3f42 85%,#555 100%)}
.quote-box{left:241px;top:2250px;width:383px;height:358px;background:var(--navy);color:var(--white);padding:26px 32px}
.quote-box p{font-style:italic;font-size:19px;line-height:34.5px;text-align:justify;font-weight:300}
.quote-name{display:inline-block;margin-top:18px;font-size:22px;border-bottom:1px solid var(--white);line-height:1.3;padding:0 2px}

/* newsletter */
.news{left:0;top:2783px;width:1200px;height:274px;background:linear-gradient(90deg,#b51a36 0%,#c8203f 40%,#c21c3b 100%)}
.news-title{top:70px;font-size:32px;color:var(--white)}
.news-form{left:329px;top:138px;width:542px;height:49px;display:flex;background:var(--white);border:2px solid var(--white)}
.news-input{flex:1;display:flex;align-items:center;padding-left:16px;font-size:14px;color:#444}
.news-btn{width:148px;background:var(--navy);color:var(--white);font-weight:700;font-size:14px;display:flex;align-items:center;justify-content:center}

/* footer */
.foot-brand{left:450px;top:3150px;width:300px;display:flex;justify-content:center;align-items:center;gap:10px;font-size:20px;font-weight:600;color:var(--navy)}
.foot-rule{left:111px;width:977px;height:1px;background:var(--rule)}
.foot-divider{top:3288px;width:1px;height:176px;background:var(--rule)}
.foot-col{top:3304px;width:300px;text-align:center}
.foot-icon{width:47px;height:47px;border-radius:50%;background:var(--navy);border:2px solid var(--red);margin:0 auto;display:flex;align-items:center;justify-content:center}
.foot-col h4{font-weight:400;font-size:21px;margin-top:12px;color:var(--ink)}
.foot-col p{font-size:14px;line-height:25px;color:var(--muted);margin-top:6px;font-weight:300}
.copyright{top:3513px;width:1200px;text-align:center;font-size:13px;color:#444}
</style>
</head>
<body>

<header class="abs hero" role="img" aria-label="Photo of a freshly painted commercial building with palm trees under a blue sky"></header>
<div class="abs brand"><span class="brand-dot"></span><span class="brand-text">Keystone Pro Co</span></div>
<nav class="abs nav">
  <a class="active">Home</a><a>About Us</a><a>Our Services</a><a>Gallery</a><a>Contact</a>
</nav>
<div class="abs btn call">
  <svg width="13" height="13" viewBox="0 0 24 24"><path fill="#fff" d="M6.6 10.8a15 15 0 0 0 6.6 6.6l2.2-2.2a1 1 0 0 1 1-.25 11.4 11.4 0 0 0 3.6.57 1 1 0 0 1 1 1V20a1 1 0 0 1-1 1A17 17 0 0 1 3 4a1 1 0 0 1 1-1h3.5a1 1 0 0 1 1 1c0 1.25.2 2.45.57 3.57a1 1 0 0 1-.25 1z"/></svg>
  Call Now
</div>
<div class="abs hero-box">
  <h1 class="hero-title">KEYSTONE PRO CO</h1>
  <p class="hero-text">Lorem ipsum dolor sit amet, consectetur adipiscing elit, sed do eiusmod tempor incididunt ut labore et dolore</p>
  <div class="btn estimate">Request for Estimate</div>
</div>

<h2 class="abs section-title who-title">Who We Are</h2>
<p class="abs who-text">Lorem ipsum dolor sit amet, consectetur adipiscing elit, sed do eiusmod tempor incididunt ut labore et dolore magna aliqua. Ut enim ad minim veniam, quis nostrud exercitation ullamco laboris nisi ut aliquip ex ea commodo consequat. Duis aute irure dolor in reprehenderit in voluptate velit esse cillum dolore eu fugiat nulla pariatur. Excepteur sint occaecat cupidatat non proident, sunt in culpa qui officia deserunt mollit anim id est laborum.</p>

<div class="abs work-photo" role="img" aria-label="Photo of a painter in a high-visibility shirt working from a lift basket against a pale wall"></div>

<section class="abs services">
  <h2 class="abs section-title services-title">Our Services</h2>
  <div class="abs service-divider"></div>
  <div class="abs service" style="left:145px">
    <div class="service-icon">
    <svg width="72" height="74" viewBox="0 0 72 74" fill="#fff"><rect x="8" y="10" width="26" height="62"/><rect x="14" y="2" width="10" height="8"/><rect x="36" y="26" width="28" height="46"/><rect x="0" y="70" width="72" height="4"/><g fill="#022a6b"><rect x="13" y="18" width="5" height="6"/><rect x="23" y="18" width="5" height="6"/><rect x="13" y="30" width="5" height="6"/><rect x="23" y="30" width="5" height="6"/><rect x="13" y="42" width="5" height="6"/><rect x="23" y="42" width="5" height="6"/><rect x="17" y="56" width="8" height="14"/><rect x="42" y="34" width="6" height="6"/><rect x="52" y="34" width="6" height="6"/><rect x="42" y="46" width="6" height="6"/><rect x="52" y="46" width="6" height="6"/><rect x="42" y="58" width="6" height="6"/><rect x="52" y="58" width="6" height="6"/></g></svg>
    </div>
    <h3>Commercial</h3>
    <p>Lorem ipsum dolor sit amet, conse ctetur adipiscing elit, sed do eiusmod tempor</p>
  </div>
  <div class="abs service" style="left:633px">
    <div class="service-icon">
    <svg width="68" height="70" viewBox="0 0 68 70" fill="#fff"><rect x="50" y="0" width="12" height="30"/><path d="M0 20l18 12V20l18 12V20l32 14v36H0z"/><g fill="#022a6b"><rect x="10" y="44" width="7" height="7"/><rect x="10" y="55" width="7" height="15"/><rect x="34" y="44" width="7" height="7"/><rect x="46" y="44" width="7" height="7"/><rect x="34" y="56" width="7" height="7"/><rect x="46" y="56" width="7" height="7"/></g></svg>
    </div>
    <h3>Industrial</h3>
    <p>Lorem ipsum dolor sit amet, conse ctetur adipiscing elit, sed do eiusmod tempor</p>
  </div>
</section>

<h2 class="abs section-title test-title">Testimonials</h2>
<div class="abs test-photo" role="img" aria-label="Photo of a newly painted commercial storefront with a black fence"></div>
<blockquote class="abs quote-box">
  <p>“Lorem ipsum dolor sit amet, conse ctetur adipiscing elit, sed do eiusmod tempor incididunt ut labore et dolore magna aliqua. Ut enim ad minim veniam, quis nostrud exercitation ullamco laboris nisi ut aliquip”</p>
  <span class="quote-name">John Doe</span>
</blockquote>

<section class="abs news" role="img" aria-label="Faint red-tinted photo of workers on a painting lift">
  <h2 class="abs section-title news-title">Subscribe Our Newsletter</h2>
  <div class="abs news-form">
    <div class="news-input">Email address</div>
    <div class="news-btn">SUBSCRIBE</div>
  </div>
</section>

<div class="abs foot-brand"><span class="brand-dot"></span>Keystone Pro Co</div>
<div class="abs foot-rule" style="top:3267px"></div>
<div class="abs foot-divider" style="left:422px"></div>
<div class="abs foot-divider" style="left:785px"></div>
<div class="abs foot-col" style="left:123px">
  <div class="foot-icon"><svg width="14" height="16" viewBox="0 0 24 24"><path fill="#fff" d="M12 2a7 7 0 0 0-7 7c0 5 7 13 7 13s7-8 7-13a7 7 0 0 0-7-7zm0 9.5A2.5 2.5 0 1 1 12 6.5a2.5 2.5 0 0 1 0 5z"/></svg></div>
  <h4>Location</h4>
  <p>123, Lorem ipsum dolor<br>sit amet</p>
</div>
<div class="abs foot-col" style="left:450px">
  <div class="foot-icon"><svg width="14" height="14" viewBox="0 0 24 24"><path fill="#fff" d="M6.6 10.8a15 15 0 0 0 6.6 6.6l2.2-2.2a1 1 0 0 1 1-.25 11.4 11.4 0 0 0 3.6.57 1 1 0 0 1 1 1V20a1 1 0 0 1-1 1A17 17 0 0 1 3 4a1 1 0 0 1 1-1h3.5a1 1 0 0 1 1 1c0 1.25.2 2.45.57 3.57a1 1 0 0 1-.25 1z"/></svg></div>
  <h4>Contact</h4>
  <p>+1 888 888 8888<br>hello@keystonepro.example</p>
</div>
<div class="abs foot-col" style="left:777px">
  <div class="foot-icon"><svg width="14" height="12" viewBox="0 0 24 20"><path fill="#fff" d="M2 2h20v16H2z"/><path d="M2 3l10 8 10-8" stroke="#022a6b" stroke-width="2" fill="none"/></svg></div>
  <h4>Follow us</h4>
  <p>Social Page<br>Photo Feed</p>
</div>
<div class="abs foot-rule" style="top:3483px"></div>
<p class="abs copyright">© Copyrights 2023 Keystone Pro Co &nbsp;| All Rights Reserved</p>

</body>
</html>
```